Create a new website for "The Arcade at Fernbrook"

I need a website for a shopping center in Atlanta USA. I want a classy high end look with high end motion videos (which I will provide).
The purpose of website is to attract new tenants to fill up vacant office spaces we have.
we will highlight existing cool stores and advertise that this is a cool place to start a new tenants business or office . ideally IT businesses in Alpharetta city in Georgia state in USA

Target Market(s)

commercial office tenants

Industry/Entity Type

Real Estate

Contact Information for Business Card

classy high end design
Arcade at Fernbrook
address:
2870 Briarwell Pkwy
Alpharetta GA 30005

Logo Text

I am open. Anything that attracts new IT tech tenants to lease up shopping center/ office space

Coding

Coded - Design and coding required

Number of Pages Required

5+ page

Requirements
Must have
• easy to browse

here is a link to some photos. i will provide videos shortly

http://www.tomsereph.com/2014/04/Building-Photos-3/n-5N2dg/
Nice to have
• please look at some of mall websites i like. Moving videos and images on home page

I really like this one: https://www.plazaatcresthollow.com/

others are

https://lindorecenter.com/

https://www.discoverbrisket.com/

```html
<!DOCTYPE html>
<html lang="en">
<head>
<meta charset="utf-8">
<title>The Arcade at Fernbrook — Office Space for Lease</title>
<link rel="stylesheet" href="https://fonts.googleapis.com/css2?family=Poppins:wght@300;400;500;600;700&display=swap">
<style>
:root{
  --blue:#1199f3;
  --ink:#222222;
  --muted:#8a8a8a;
  --soft:#f3f3f3;
  --footer:#333333;
  --white:#ffffff;
  --heart:#e8392f;
}
*{box-sizing:border-box;margin:0;padding:0}
html,body{width:1200px;height:3727px;overflow:hidden}
body{font-family:'Poppins',sans-serif;color:var(--ink);background:var(--white);position:relative}
.abs{position:absolute}
a{color:inherit;text-decoration:none}

/* hero */
.hero{left:0;top:0;width:1200px;height:579px;overflow:hidden}
.hero-photo{position:absolute;inset:0;background:
  radial-gradient(ellipse 180px 120px at 600px 40px,rgba(170,200,215,.9),transparent 70%),
  radial-gradient(ellipse 260px 180px at 600px 470px,rgba(232,190,140,.85),transparent 70%),
  radial-gradient(ellipse 200px 260px at 1080px 420px,rgba(40,50,110,.9),transparent 70%),
  radial-gradient(ellipse 200px 220px at 140px 470px,rgba(60,40,30,.95),transparent 70%),
  radial-gradient(ellipse 220px 160px at 180px 200px,rgba(205,200,190,.8),transparent 70%),
  radial-gradient(ellipse 220px 160px at 1020px 200px,rgba(200,195,185,.8),transparent 70%),
  linear-gradient(180deg,#5d6d74 0%,#a69a88 30%,#9a8268 55%,#6a4e36 80%,#3e2c20 100%)}
.hero-shade{position:absolute;inset:0;background:rgba(0,0,0,.18)}
.brand{left:148px;top:34px;color:var(--white);font-weight:500;font-size:17px;letter-spacing:.3px}
.nav{left:527px;top:38px;display:flex;gap:29px;color:var(--white);font-size:11px;font-weight:500}
.search{left:966px;top:37px}
.hero-title{left:0;width:1200px;top:222px;text-align:center;color:var(--white);font-weight:700;font-size:47px;line-height:44px;text-transform:uppercase}
.hero-btn{left:501px;top:342px;width:198px;height:45px;background:var(--blue);color:var(--white);font-weight:600;font-size:18px;display:flex;align-items:center;justify-content:center}

.section-title{left:0;width:1200px;text-align:center;font-weight:500;font-size:23px;text-transform:uppercase}

/* listing cards */
.listing{width:214px;height:240px;overflow:hidden;color:var(--white)}
.listing-photo{position:absolute;inset:0}
.tone-a{background:
  radial-gradient(circle 40px at 60px 95px,rgba(200,170,110,.8),transparent 80%),
  radial-gradient(circle 45px at 130px 100px,rgba(190,160,100,.7),transparent 80%),
  radial-gradient(ellipse 60px 110px at 200px 120px,rgba(150,70,50,.9),transparent 80%),
  linear-gradient(180deg,#c9a050 0%,#5a4a36 12%,#4a3e32 55%,#2e2824 100%)}
.tone-b{background:
  radial-gradient(ellipse 60px 140px at 140px 90px,rgba(70,110,140,.8),transparent 80%),
  radial-gradient(ellipse 50px 60px at 80px 150px,rgba(40,40,44,.9),transparent 80%),
  linear-gradient(180deg,#c7ccd0 0%,#a8b0b6 40%,#8a9298 75%,#5d6468 100%)}
.tone-c{background:
  radial-gradient(ellipse 60px 80px at 150px 110px,rgba(180,110,50,.9),transparent 80%),
  radial-gradient(ellipse 70px 30px at 160px 170px,rgba(200,180,60,.8),transparent 80%),
  radial-gradient(ellipse 40px 90px at 40px 120px,rgba(120,80,40,.8),transparent 80%),
  linear-gradient(180deg,#8a8a84 0%,#6e6a60 30%,#5a4a36 65%,#3a342c 100%)}
.tone-d{background:
  radial-gradient(ellipse 60px 80px at 80px 110px,rgba(120,115,105,.7),transparent 80%),
  radial-gradient(ellipse 50px 40px at 170px 170px,rgba(20,20,22,.9),transparent 80%),
  linear-gradient(180deg,#6a6660 0%,#4a4640 40%,#34322e 75%,#24221f 100%)}
.listing-photo::after{content:"";position:absolute;inset:0;background:linear-gradient(180deg,rgba(0,0,0,0) 45%,rgba(0,0,0,.35) 100%)}
.fav{position:absolute;right:12px;top:12px}
.price{position:absolute;left:27px;top:141px;font-weight:600;font-size:23px}
.kind{position:absolute;left:27px;top:167px;font-size:16px}
.listing-bar{position:absolute;left:0;bottom:0;width:100%;height:36px;background:rgba(0,0,0,.55);display:flex;align-items:center;padding-left:27px;font-size:9.5px;gap:8px}
.listing-bar .sep{width:1px;height:14px;background:rgba(255,255,255,.7)}
.details{background:var(--blue);border-radius:10px;padding:3px 10px;font-weight:500;font-size:9px}
.see-all{left:544px;top:1271px;width:111px;height:37px;border-radius:19px;background:var(--blue);color:var(--white);font-weight:500;font-size:15px;display:flex;align-items:center;justify-content:center;gap:5px}

.band{left:0;width:1200px;background:var(--soft)}

/* category tiles */
.category{top:1518px;height:351px;color:var(--white);text-align:center;overflow:hidden}
.category::after{content:"";position:absolute;inset:0;background:rgba(0,0,0,.3)}
.category .num,.category .label{z-index:1}
.category .num{position:absolute;left:0;width:100%;top:134px;font-weight:600;font-size:46px;line-height:50px}
.category .label{position:absolute;left:0;width:100%;top:187px;font-size:19px}
.cat-shops{background:
  radial-gradient(ellipse 150px 40px at 147px 30px,rgba(230,225,215,.9),transparent 80%),
  radial-gradient(ellipse 160px 60px at 147px 110px,rgba(150,140,120,.8),transparent 80%),
  radial-gradient(ellipse 150px 80px at 147px 270px,rgba(190,180,165,.8),transparent 80%),
  linear-gradient(180deg,#8a8478,#5a5448 40%,#7a7264 75%,#4e4a44)}
.cat-office{background:
  radial-gradient(ellipse 120px 60px at 180px 120px,rgba(200,190,170,.7),transparent 80%),
  radial-gradient(ellipse 120px 90px at 120px 250px,rgba(110,80,50,.9),transparent 80%),
  linear-gradient(180deg,#2a2624,#5a4e40 35%,#4a3a2a 70%,#2a2420)}
.cat-apart{background:
  radial-gradient(ellipse 120px 120px at 60px 140px,rgba(220,225,230,.9),transparent 80%),
  radial-gradient(ellipse 130px 60px at 170px 300px,rgba(230,228,222,.85),transparent 80%),
  radial-gradient(ellipse 60px 90px at 240px 150px,rgba(60,60,60,.8),transparent 80%),
  linear-gradient(180deg,#9ca0a4,#b4b6b4 50%,#8c8e8a)}

/* videos */
.video{top:2080px;width:449px;height:267px;overflow:hidden}
.video::after{content:"";position:absolute;inset:0;background:rgba(0,0,0,.22)}
.play{position:absolute;left:50%;top:50%;transform:translate(-50%,-50%);z-index:1}
.vid-lounge{left:148px;background:
  radial-gradient(ellipse 70px 90px at 360px 120px,rgba(200,215,230,.9),transparent 80%),
  radial-gradient(ellipse 110px 40px at 120px 200px,rgba(230,225,215,.85),transparent 80%),
  radial-gradient(ellipse 120px 40px at 224px 30px,rgba(220,215,205,.8),transparent 80%),
  linear-gradient(180deg,#a9a49a,#7a7266 50%,#3e3a34)}
.vid-office{left:612px;background:
  radial-gradient(ellipse 200px 50px at 224px 40px,rgba(235,235,235,.9),transparent 80%),
  radial-gradient(ellipse 50px 40px at 140px 170px,rgba(30,30,30,.85),transparent 80%),
  radial-gradient(ellipse 50px 40px at 330px 190px,rgba(40,40,40,.8),transparent 80%),
  linear-gradient(180deg,#c8cac8,#a6a8a6 50%,#8a8c8a)}

/* testimonials */
.quote{width:370px;height:160px;background:var(--white)}
.avatar{position:absolute;left:27px;top:-39px;width:79px;height:79px;border-radius:50%;background:radial-gradient(circle at 50% 40%,#e2c2a8 0 22%,#6a5040 23% 35%,#9aa4ac 36%);border:3px solid var(--white)}
.quote p{position:absolute;left:27px;top:54px;width:330px;font-size:10px;line-height:15px;color:#666}
.quote .name{position:absolute;left:28px;top:112px;font-size:13px;color:var(--ink)}
.quote .role{position:absolute;left:28px;top:130px;font-size:9px;color:#aaa}
.arrow-btn{top:2787px;width:23px;height:23px;border:1px solid #bbb;display:flex;align-items:center;justify-content:center}

/* blogs */
.post{top:3015px;width:292px;height:341px;border:1px solid #ccc;background:var(--white)}
.post-photo{position:absolute;left:0;top:0;width:100%;height:162px}
.photo-tax{background:
  radial-gradient(ellipse 40px 30px at 40px 90px,rgba(240,240,235,.9),transparent 80%),
  radial-gradient(ellipse 80px 40px at 170px 100px,rgba(220,205,185,.8),transparent 80%),
  radial-gradient(ellipse 60px 60px at 240px 40px,rgba(40,50,90,.85),transparent 80%),
  linear-gradient(160deg,#4a3e34,#2e2824 50%,#7a6a58)}
.photo-plan{background:
  radial-gradient(ellipse 90px 60px at 210px 110px,rgba(245,245,245,.95),transparent 80%),
  radial-gradient(ellipse 60px 40px at 70px 30px,rgba(230,230,230,.8),transparent 80%),
  linear-gradient(160deg,#2a2c30,#4a4c50 50%,#9a9ca0)}
.photo-acct{background:
  radial-gradient(ellipse 50px 40px at 146px 60px,rgba(30,30,34,.85),transparent 80%),
  radial-gradient(ellipse 30px 40px at 250px 60px,rgba(90,130,60,.7),transparent 80%),
  radial-gradient(ellipse 30px 30px at 50px 80px,rgba(90,130,60,.6),transparent 80%),
  linear-gradient(180deg,#f0f0ee,#e0e0dc 60%,#b0b2ae)}
.post h3{position:absolute;left:24px;top:180px;font-weight:500;font-size:16px}
.post p{position:absolute;left:24px;top:208px;width:245px;font-size:10px;line-height:15px;color:#777}
.read-more{position:absolute;left:24px;top:290px;width:76px;height:26px;border-radius:13px;background:var(--blue);color:var(--white);font-size:10px;display:flex;align-items:center;justify-content:center}

/* footer */
.footer{left:0;top:3431px;width:1200px;height:246px;background:var(--footer);color:var(--white)}
.fcol{position:absolute;top:70px}
.fcol h4{font-weight:500;font-size:15px;margin-bottom:18px;text-transform:uppercase}
.fcol li{list-style:none;font-size:10.5px;margin-bottom:16px}
.contact-line{display:flex;gap:6px;font-size:10.5px;line-height:15px;margin-bottom:12px}
.newsletter{display:flex;width:217px;height:25px;border:1px solid var(--blue)}
.newsletter span{flex:1;background:var(--white);color:#aaa;font-size:9.5px;display:flex;align-items:center;padding-left:12px}
.newsletter b{width:70px;background:var(--blue);font-weight:500;font-size:10px;display:flex;align-items:center;justify-content:center}
.socials{display:flex;gap:11px;margin-top:24px}
.socials i{width:24px;height:24px;background:var(--blue);display:block}
.copyright{left:0;top:3677px;width:1200px;height:50px;background:var(--blue);color:var(--white);font-size:10.5px;font-weight:500;display:flex;align-items:center;justify-content:center}
</style>
</head>
<body>

<header class="abs hero">
  <div class="hero-photo" role="img" aria-label="Interior of a bright upscale shopping arcade with storefronts and a glass roof"></div>
  <div class="hero-shade"></div>
  <div class="abs brand">ARCADE AT FERNBROOK</div>
  <nav class="abs nav"><a>HOME</a><a>ABOUT US</a><a>LISTING</a><a>BLOGS</a><a>CONTACT US</a></nav>
  <svg class="abs search" width="15" height="15" viewBox="0 0 15 15" fill="none" stroke="#fff" stroke-width="1.5"><circle cx="6" cy="6" r="4.8"/><path d="M9.6 9.6 14 14"/></svg>
  <h1 class="abs hero-title">Find the best place<br>for your office</h1>
  <a class="abs hero-btn">Contact Us</a>
</header>

<h2 class="abs section-title" style="top:652px">Featured Listing</h2>

<article class="abs listing" style="left:148px;top:715px"><div class="listing-photo tone-a" role="img" aria-label="Office with hexagon shelves and brick wall"></div>
  <svg class="fav" width="30" height="30" viewBox="0 0 30 30"><circle cx="15" cy="15" r="13.5" fill="none" stroke="#fff" stroke-width="2"/><path d="M15 21 9.5 15.6a3.4 3.4 0 0 1 5.5-4 3.4 3.4 0 0 1 5.5 4Z" fill="var(--heart)"/></svg>
  <div class="price">$105.00</div><div class="kind">Office Space</div>
  <div class="listing-bar">15 Chair<span class="sep"></span>45000 SF<span class="sep"></span><span class="details">Details</span></div></article>
<article class="abs listing" style="left:381px;top:715px"><div class="listing-photo tone-b" role="img" aria-label="Bright office with patterned wall and desk chair"></div>
  <svg class="fav" width="30" height="30" viewBox="0 0 30 30"><circle cx="15" cy="15" r="13.5" fill="none" stroke="#fff" stroke-width="2"/><path d="M15 21 9.5 15.6a3.4 3.4 0 0 1 5.5-4 3.4 3.4 0 0 1 5.5 4Z" fill="#fff"/></svg>
  <div class="price">$105.00</div><div class="kind">Office Space</div>
  <div class="listing-bar">15 Chair<span class="sep"></span>45000 SF<span class="sep"></span><span class="details">Details</span></div></article>
<article class="abs listing" style="left:614px;top:715px"><div class="listing-photo tone-c" role="img" aria-label="Lounge with wood panelling and yellow sofa"></div>
  <svg class="fav" width="30" height="30" viewBox="0 0 30 30"><circle cx="15" cy="15" r="13.5" fill="none" stroke="#fff" stroke-width="2"/><path d="M15 21 9.5 15.6a3.4 3.4 0 0 1 5.5-4 3.4 3.4 0 0 1 5.5 4Z" fill="#fff"/></svg>
  <div class="price">$105.00</div><div class="kind">Office Space</div>
  <div class="listing-bar">15 Chair<span class="sep"></span>45000 SF<span class="sep"></span><span class="details">Details</span></div></article>
<article class="abs listing" style="left:847px;top:715px"><div class="listing-photo tone-d" role="img" aria-label="Dark meeting room with black chairs"></div>
  <svg class="fav" width="30" height="30" viewBox="0 0 30 30"><circle cx="15" cy="15" r="13.5" fill="none" stroke="#fff" stroke-width="2"/><path d="M15 21 9.5 15.6a3.4 3.4 0 0 1 5.5-4 3.4 3.4 0 0 1 5.5 4Z" fill="#fff"/></svg>
  <div class="price">$105.00</div><div class="kind">Office Space</div>
  <div class="listing-bar">15 Chair<span class="sep"></span>45000 SF<span class="sep"></span><span class="details">Details</span></div></article>

<article class="abs listing" style="left:148px;top:976px"><div class="listing-photo tone-a" role="img" aria-label="Office with hexagon shelves and brick wall"></div>
  <svg class="fav" width="30" height="30" viewBox="0 0 30 30"><circle cx="15" cy="15" r="13.5" fill="none" stroke="#fff" stroke-width="2"/><path d="M15 21 9.5 15.6a3.4 3.4 0 0 1 5.5-4 3.4 3.4 0 0 1 5.5 4Z" fill="var(--heart)"/></svg>
  <div class="price">$105.00</div><div class="kind">Office Space</div>
  <div class="listing-bar">15 Chair<span class="sep"></span>45000 SF<span class="sep"></span><span class="details">Details</span></div></article>
<article class="abs listing" style="left:381px;top:976px"><div class="listing-photo tone-b" role="img" aria-label="Bright office with patterned wall and desk chair"></div>
  <svg class="fav" width="30" height="30" viewBox="0 0 30 30"><circle cx="15" cy="15" r="13.5" fill="none" stroke="#fff" stroke-width="2"/><path d="M15 21 9.5 15.6a3.4 3.4 0 0 1 5.5-4 3.4 3.4 0 0 1 5.5 4Z" fill="#fff"/></svg>
  <div class="price">$105.00</div><div class="kind">Office Space</div>
  <div class="listing-bar">15 Chair<span class="sep"></span>45000 SF<span class="sep"></span><span class="details">Details</span></div></article>
<article class="abs listing" style="left:614px;top:976px"><div class="listing-photo tone-c" role="img" aria-label="Lounge with wood panelling and yellow sofa"></div>
  <svg class="fav" width="30" height="30" viewBox="0 0 30 30"><circle cx="15" cy="15" r="13.5" fill="none" stroke="#fff" stroke-width="2"/><path d="M15 21 9.5 15.6a3.4 3.4 0 0 1 5.5-4 3.4 3.4 0 0 1 5.5 4Z" fill="#fff"/></svg>
  <div class="price">$105.00</div><div class="kind">Office Space</div>
  <div class="listing-bar">15 Chair<span class="sep"></span>45000 SF<span class="sep"></span><span class="details">Details</span></div></article>
<article class="abs listing" style="left:847px;top:976px"><div class="listing-photo tone-d" role="img" aria-label="Dark meeting room with black chairs"></div>
  <svg class="fav" width="30" height="30" viewBox="0 0 30 30"><circle cx="15" cy="15" r="13.5" fill="none" stroke="#fff" stroke-width="2"/><path d="M15 21 9.5 15.6a3.4 3.4 0 0 1 5.5-4 3.4 3.4 0 0 1 5.5 4Z" fill="#fff"/></svg>
  <div class="price">$105.00</div><div class="kind">Office Space</div>
  <div class="listing-bar">15 Chair<span class="sep"></span>45000 SF<span class="sep"></span><span class="details">Details</span></div></article>

<a class="abs see-all">See All <svg width="13" height="10" viewBox="0 0 13 10" fill="none" stroke="#fff" stroke-width="1.4"><path d="M0 5h12M8 1l4 4-4 4"/></svg></a>

<section class="abs band" style="top:1384px;height:560px"></section>
<h2 class="abs section-title" style="top:1456px">What we are looking</h2>
<div class="abs category cat-shops" style="left:148px;width:294px" role="img" aria-label="Multi-level shopping mall atrium with shoppers">
  <div class="num">500+</div><div class="label">Shops</div></div>
<div class="abs category cat-office" style="left:457px;width:294px" role="img" aria-label="Busy open-plan office with people at desks">
  <div class="num">100+</div><div class="label">Office Space</div></div>
<div class="abs category cat-apart" style="left:766px;width:295px" role="img" aria-label="Modern apartment living room with sofa">
  <div class="num">200+</div><div class="label">Apartments</div></div>

<h2 class="abs section-title" style="top:2017px">Videos</h2>
<div class="abs video vid-lounge" role="img" aria-label="Video preview of a furnished lounge with tall windows">
  <svg class="play" width="72" height="72" viewBox="0 0 72 72"><circle cx="36" cy="36" r="34" fill="rgba(255,255,255,.2)" stroke="#fff" stroke-width="2"/><path d="M29 24v24l20-12Z" fill="#fff"/></svg></div>
<div class="abs video vid-office" role="img" aria-label="Video preview of an open office with desks and chairs">
  <svg class="play" width="72" height="72" viewBox="0 0 72 72"><circle cx="36" cy="36" r="34" fill="rgba(255,255,255,.2)" stroke="#fff" stroke-width="2"/><path d="M29 24v24l20-12Z" fill="#fff"/></svg></div>

<section class="abs band" style="top:2423px;height:462px"></section>
<h2 class="abs section-title" style="top:2495px">Testimonials</h2>
<div class="abs" style="left:0;top:2540px;width:1200px;height:240px;overflow:hidden">
  <div class="abs quote" style="left:148px;top:58px"><div class="avatar" role="img" aria-label="Portrait of the reviewer"></div>
    <p>Lorem Ipsum is simply dummy text of the printing and typesetting industry. Lorem Ipsum has been the industry's standard dummy text ever since the 1500s,</p>
    <div class="name">John Doe</div><div class="role">Manager</div></div>
  <div class="abs quote" style="left:534px;top:58px"><div class="avatar" role="img" aria-label="Portrait of the reviewer"></div>
    <p>Lorem Ipsum is simply dummy text of the printing and typesetting industry. Lorem Ipsum has been the industry's standard dummy text ever since the 1500s,</p>
    <div class="name">John Doe</div><div class="role">Manager</div></div>
  <div class="abs quote" style="left:921px;top:58px"><div class="avatar" role="img" aria-label="Portrait of the reviewer"></div>
    <p>Lorem Ipsum is simply dummy text of the printing and typesetting industry. Lorem Ipsum has been the industry's standard dummy text ever since the 1500s,</p>
    <div class="name">John Doe</div><div class="role">Manager</div></div>
</div>
<div class="abs arrow-btn" style="left:1009px"><svg width="7" height="10" viewBox="0 0 7 10" fill="none" stroke="#888" stroke-width="1.2"><path d="M6 1 2 5l4 4"/></svg></div>
<div class="abs arrow-btn" style="left:1038px"><svg width="7" height="10" viewBox="0 0 7 10" fill="none" stroke="#888" stroke-width="1.2"><path d="M1 1l4 4-4 4"/></svg></div>

<h2 class="abs section-title" style="top:2952px">Our Blogs</h2>
<article class="abs post" style="left:149px"><div class="post-photo photo-tax" role="img" aria-label="People working with paperwork and coffee"></div>
  <h3>Tax Planning &amp; Preparation</h3>
  <p>Lorem Ipsum is simply dummy text of the printing and typesetting industry. Lorem Ipsum has been the industry's standard dummy text ever since the 1500s,</p>
  <a class="read-more">Read More</a></article>
<article class="abs post" style="left:459px"><div class="post-photo photo-plan" role="img" aria-label="Laptop keyboard beside printed charts"></div>
  <h3 style="top:185px">Construction Investment plan</h3>
  <p style="top:211px">Lorem Ipsum is simply dummy text of the printing and typesetting industry. Lorem Ipsum has been the industry's standard dummy text ever since the 1500s,</p>
  <a class="read-more">Read More</a></article>
<article class="abs post" style="left:769px"><div class="post-photo photo-acct" role="img" aria-label="Desktop computer on a desk with plants"></div>
  <h3>Small Business Accounting</h3>
  <p>Lorem Ipsum is simply dummy text of the printing and typesetting industry. Lorem Ipsum has been the industry's standard dummy text ever since the 1500s,</p>
  <a class="read-more">Read More</a></article>

<footer class="abs footer">
  <div class="fcol" style="left:148px"><h4>Information</h4><ul><li>Help &amp; FAQs</li><li>Advance Search</li><li>Gift Cards</li><li>Shop By Brands</li></ul></div>
  <div class="fcol" style="left:381px"><h4>Account</h4><ul><li>Preference</li><li>Order history</li><li>Cart Page</li><li>Sign In</li></ul></div>
  <div class="fcol" style="left:612px"><h4>Contact</h4>
    <div class="contact-line"><svg width="8" height="11" viewBox="0 0 8 11"><path d="M4 0a4 4 0 0 1 4 4c0 3-4 7-4 7S0 7 0 4a4 4 0 0 1 4-4Z" fill="var(--blue)"/><circle cx="4" cy="4" r="1.4" fill="#333"/></svg><span>2870 Briarwell Pkwy,<br>Alpharetta GA 30005</span></div>
    <div class="contact-line"><svg width="8" height="11" viewBox="0 0 8 11"><path d="M1 0h2l1 3-1.5 1a6 6 0 0 0 2.5 3L6 5.5l2 1V9c0 1-1 2-2 1.5C3 9 1 6 0 2 0 1 .5 0 1 0Z" fill="var(--blue)"/></svg><span>1-800-555-0142</span></div>
    <div class="contact-line"><svg width="10" height="11" viewBox="0 0 10 11"><rect x="0" y="2.5" width="10" height="7" fill="var(--blue)"/><path d="M0 3l5 3.5L10 3" stroke="#333" fill="none"/></svg><span>leasing@fernbrookarcade.com</span></div>
  </div>
  <div class="fcol" style="left:844px"><h4>Newsletter</h4>
    <div class="newsletter"><span>Enter Email</span><b>Subscribe</b></div>
    <div class="socials" aria-label="Social links"><i></i><i></i><i></i><i></i></div>
  </div>
</footer>
<div class="abs copyright">Copyright 2020-2030.Reserved all rights</div>

</body>
</html>
```